Business Cards, Letterhead, Corporate Materials

Harlow Building Partners, Inc. needs brand identity and marketing materials.

Target Market(s)

Home Owners, Architects, Engineers.

Contact Information for Business Card

Business Cards for myself the President

Font styles to use
Serif

Colors
3377b5
0255a3
cfdfed
cee9f5
86cae7
0393ce
000000
ffffff
f5f5f5

Requirements
Must have
• My name, my address, my email, phone number, company logo, my title. my contractor's license number, web address.
Nice to have
• Very clean professional modern business cards for company president.

```html
<!DOCTYPE html>
<html lang="en">
<head>
<meta charset="utf-8">
<title>Harlow Building Partners, Inc. – Business Card</title>
<link href="https://fonts.googleapis.com/css2?family=Arimo:wght@400;700&display=swap" rel="stylesheet">
<style>
  :root {
    --brand-blue: #2457a0;
    --brand-deep: #0255a3;
    --wave-top: #234a8f;
    --wave-bottom: #2e9bd0;
    --swoosh-grey: #7d848c;
    --ink: #231f20;
    --muted: #808285;
    --border: #6d6e70;
    --white: #ffffff;
    --page: #ffffff;
  }
  * { box-sizing: border-box; margin: 0; padding: 0; }
  html, body {
    width: 938px; height: 1200px; overflow: hidden;
    background: var(--page);
    font-family: "Arimo", Arial, sans-serif;
  }
  .sheet { position: relative; width: 938px; height: 1200px; }
  .card {
    position: absolute; left: 0; width: 936px; height: 536px;
    border: 1px solid var(--border); border-radius: 45px;
    overflow: hidden; background: var(--white);
  }
  .card--front { top: 0; }
  .card--back { top: 580px; }
  .card__wave { position: absolute; inset: 0; width: 100%; height: 100%; }
  .registration {
    position: absolute; right: 65px; bottom: 44px;
    text-align: right; color: var(--white);
    font-weight: 700; font-size: 26px; line-height: 34px;
  }
  .brand { position: absolute; display: flex; align-items: center; }
  .brand__mark { background: var(--brand-deep); flex: none; }
  .brand__name {
    color: var(--brand-blue); font-weight: 700; text-transform: uppercase;
    line-height: 1.05; letter-spacing: 0.5px;
  }
  .card--front .brand { left: 89px; top: 94px; }
  .card--front .brand__mark { width: 138px; height: 138px; margin-right: 28px; }
  .card--front .brand__name { font-size: 46px; }
  .card--back .brand { left: 488px; top: 64px; }
  .card--back .brand__mark { width: 83px; height: 83px; margin-right: 16px; }
  .card--back .brand__name { font-size: 27px; }
  .holder { position: absolute; left: 71px; top: 92px; }
  .holder__name { font-size: 36px; font-weight: 700; color: var(--ink); line-height: 42px; }
  .holder__title { font-size: 27px; color: var(--muted); line-height: 34px; }
  .contacts { position: absolute; left: 71px; top: 228px; list-style: none; }
  .contacts li {
    display: flex; align-items: center; height: 43px;
    font-size: 27px; color: var(--ink);
  }
  .contacts svg { width: 32px; height: 28px; margin-right: 21px; fill: var(--muted); flex: none; }
</style>
</head>
<body>
<main class="sheet">

  <section class="card card--front">
    <svg class="card__wave" viewBox="0 0 936 536" aria-hidden="true">
      <defs>
        <linearGradient id="waveFront" x1="0" y1="0" x2="0" y2="1">
          <stop offset="0" stop-color="#234a8f"/>
          <stop offset="1" stop-color="#2e9bd0"/>
        </linearGradient>
      </defs>
      <path d="M0,433 C330,482 720,392 936,190 L936,536 L0,536 Z" fill="url(#waveFront)"/>
      <path d="M22,428 C330,448 690,362 892,205 C710,372 360,474 22,428 Z" fill="#7d848c"/>
    </svg>
    <div class="brand">
      <span class="brand__mark"></span>
      <span class="brand__name">Harlow Building<br>Partners, Inc.</span>
    </div>
    <p class="registration">ABN: 11 222 333 444<br>Licence: 10000000</p>
  </section>

  <section class="card card--back">
    <svg class="card__wave" viewBox="0 0 936 536" aria-hidden="true">
      <defs>
        <linearGradient id="waveBack" x1="0" y1="0" x2="0" y2="1">
          <stop offset="0" stop-color="#234a8f"/>
          <stop offset="1" stop-color="#2e9bd0"/>
        </linearGradient>
      </defs>
      <path d="M0,433 C330,482 720,392 936,190 L936,536 L0,536 Z" fill="url(#waveBack)"/>
      <path d="M22,428 C330,448 690,362 892,205 C710,372 360,474 22,428 Z" fill="#7d848c"/>
    </svg>
    <div class="brand">
      <span class="brand__mark"></span>
      <span class="brand__name">Harlow Building<br>Partners, Inc.</span>
    </div>
    <div class="holder">
      <h1 class="holder__name">Person name</h1>
      <p class="holder__title">President</p>
    </div>
    <ul class="contacts">
      <li>
        <svg viewBox="0 0 32 28" aria-hidden="true"><path d="M2,12 C2,4 30,4 30,12 L30,15 L23,15 L23,11 C20,9 12,9 9,11 L9,15 L2,15 Z"/><ellipse cx="16" cy="19" rx="9" ry="6"/><circle cx="16" cy="19" r="3" fill="#fff"/></svg>
        (0123) 1230-4506
      </li>
      <li>
        <svg viewBox="0 0 32 28" aria-hidden="true"><path d="M10,1 h12 a3,3 0 0 1 3,3 v20 a3,3 0 0 1 -3,3 h-12 a3,3 0 0 1 -3,-3 v-20 a3,3 0 0 1 3,-3 Z M10,4 v17 h12 v-17 Z"/><circle cx="16" cy="24" r="1.5" fill="#fff"/></svg>
        (0123) 1230-4506
      </li>
      <li>
        <svg viewBox="0 0 32 28" aria-hidden="true"><path d="M1,6 h30 v16 h-30 Z"/><path d="M2,7 L16,17 L30,7" fill="none" stroke="#fff" stroke-width="2"/><path d="M2,21 L12,13 M30,21 L20,13" stroke="#fff" stroke-width="1.5"/></svg>
        person@harlowbuilding.com
      </li>
      <li>
        <svg viewBox="0 0 32 28" aria-hidden="true"><g fill="none" stroke="#808285" stroke-width="2"><circle cx="16" cy="14" r="12"/><ellipse cx="16" cy="14" rx="5" ry="12"/><path d="M4,14 h24 M6,8 h20 M6,20 h20"/></g></svg>
        www.harlowbuilding.com
      </li>
    </ul>
    <p class="registration">ABN: 11 222 333 444<br>Licence: 10000000</p>
  </section>

</main>
</body>
</html>
```